Brake Test Training for Coal Mining

We offer Brake Test Training for Coal Mine workers. It's a legislative requirement that workers who are tasked with performing brake testing have certain competencies to do so. We test Light Vehicles and trailers, Heavy Vehicles and Mobile Mining Equipment like Graders, Scrapers and Dump Trucks.

```html
<!DOCTYPE html>
<html lang="en">
<head>
<meta charset="utf-8">
<title>Brake Test Training for Coal Mining – Billboard</title>
<link rel="stylesheet" href="https://fonts.googleapis.com/css2?family=Bebas+Neue&family=Montserrat:wght@700&display=swap">
<style>
  :root {
    --navy: #233170;
    --gold: #f2be3c;
    --white: #ffffff;
    --paper: #f3f3f5;
    --stage: #d9d9d9;
    --photo-light: #d9b25a;
    --photo-dark: #5a4a2c;
  }
  html, body {
    margin: 0;
    width: 1200px;
    height: 1200px;
    overflow: hidden;
    background: var(--stage);
  }
  .billboard {
    position: absolute;
    left: 40px;
    top: 320px;
    width: 1120px;
    height: 560px;
    display: block;
  }
  .panel-white { fill: var(--white); }
  .band-gold { fill: var(--gold); }
  .band-navy { fill: var(--navy); }
  .brand-rule-navy { stroke: var(--navy); stroke-width: 4; }
  .brand-rule-gold { stroke: var(--gold); stroke-width: 4; }
  .brand-dot { fill: var(--navy); }
  .brand-name {
    font-family: "Montserrat", Arial, sans-serif;
    font-weight: 700;
    fill: var(--navy);
    letter-spacing: 2px;
  }
  .headline {
    font-family: "Bebas Neue", "Arial Narrow", sans-serif;
  }
  .headline-main { fill: var(--gold); font-size: 262px; }
  .headline-sub { fill: var(--white); font-size: 122px; }
  .headline-tail { fill: var(--white); font-size: 100px; }
  .phone-badge { fill: var(--navy); }
  .phone-icon { fill: var(--gold); }
  .phone-number {
    font-family: "Bebas Neue", "Arial Narrow", sans-serif;
    fill: var(--navy);
    font-size: 108px;
  }
</style>
</head>
<body>
<svg class="billboard" viewBox="0 0 1240 620" xmlns="http://www.w3.org/2000/svg">
  <defs>
    <linearGradient id="truck-tone" x1="0" y1="0" x2="0" y2="1">
      <stop offset="0" stop-color="var(--photo-light)"/>
      <stop offset="1" stop-color="var(--photo-dark)"/>
    </linearGradient>
  </defs>

  <rect class="panel-white" x="0" y="0" width="1240" height="620"/>
  <polygon class="band-gold" points="595,0 1240,0 1240,620 418,620"/>
  <polygon class="band-navy" points="615,0 1240,0 1240,470 481,470"/>

  <g class="brand">
    <circle class="brand-dot" cx="100" cy="110" r="40"/>
    <line class="brand-rule-navy" x1="165" y1="70" x2="440" y2="70"/>
    <text class="brand-name" x="188" y="108" font-size="25" textLength="250">RIDGELINE</text>
    <text class="brand-name" x="222" y="136" font-size="15" textLength="180">OPERATOR TRAINING</text>
    <line class="brand-rule-gold" x1="165" y1="148" x2="440" y2="148"/>
  </g>

  <rect class="truck-photo" x="40" y="190" width="630" height="400" rx="24" fill="url(#truck-tone)"
        role="img" aria-label="Photo of a large yellow mining dump truck loaded with coal"/>

  <g class="headline">
    <text class="headline-main" x="700" y="228" textLength="495" lengthAdjust="spacingAndGlyphs">BRAKE</text>
    <text class="headline-sub" x="700" y="336" textLength="495" lengthAdjust="spacingAndGlyphs">TEST TRAINING</text>
    <text class="headline-tail" x="700" y="431" textLength="432" lengthAdjust="spacingAndGlyphs">FOR COAL MINING</text>
  </g>

  <g class="contact">
    <circle class="phone-badge" cx="750" cy="544" r="45"/>
    <path class="phone-icon" d="M733 522c3-3 7-3 9 0l6 8c2 3 1 6-1 8l-3 3c2 6 7 11 13 13l3-3c2-2 5-3 8-1l8 6c3 2 3 6 0 9l-4 4c-5 5-17 2-29-10s-15-24-10-29z"/>
    <text class="phone-number" x="820" y="584" textLength="375" lengthAdjust="spacingAndGlyphs">1300 555 018</text>
  </g>
</svg>
</body>
</html>
```